Quillby Housecrafters Door Hanger design, Postcard and presentation folders Design

we are a home improvement company in Portland Oregon, are main service is roofing but we also do gutters, painting and pressure washing. we are a certified roofing contractor for TRV. We have over 20years of experince in the roofing industry we use top quality materials. Our mission is to do quality work and provide the best service.
Updates

This door hangers are going to be share to homeowners where we are currently working at! I will like to have a square maybe 2 inch wide and 1 inch hide (blank) for me to put the address where we are working at. So we want to give a direct message to homeowners who we are and why we are there for. Our services are roofing, gutters, painting, and pressure washing. But 95% of the door hangers should give the message that we are a roofing contractor. We are also certified by TRV which means all of our new roof projects have a 50 year warranty which only 2% of roofing contractor can offer that. We also offer finance, and all quality work. I will like to add photos of our trucks since all of them are wrap which will build them trust.

Target Market(s)

This door hangers should be custom for Homeowners with residential Homes,,, Average customer are between 40 & 65 Years old.

Industry/Entity Type

Roofing

Contact Information for Business Card

Logo, name, phone number, credentials, and services like roofing gutters painting and pressure washing

Font styles to use
Serif
Sans Serif
Decorative

Colors
33b8a4
5c5c5c

Requirements
Must have
• I want tho have a folder design just like this business card sample i uploaded. Teal and charcoal with services ...
Nice to have
• company trucks, job photo, crew photo and credential photos
Should not have
• I dont want it too busy or crowded..

```html
<!DOCTYPE html>
<html lang="en">
<head>
<meta charset="utf-8">
<title>Quillby Housecrafters – Door Hangers</title>
<link rel="stylesheet" href="https://fonts.googleapis.com/css2?family=Roboto+Slab:wght@400;600;700;800&family=Open+Sans:wght@400;600;700&display=swap">
<style>
  :root{
    --teal:#33b8a4;
    --charcoal:#5c5c5c;
    --white:#ffffff;
    --page:#1b1b1b;
    --ink:#2e2e2e;
    --line:#8a8a8a;
    --award:#33a86a;
    --slab:"Roboto Slab", Georgia, serif;
    --sans:"Open Sans", Arial, sans-serif;
  }
  *{box-sizing:border-box;margin:0;padding:0}
  html,body{width:1200px;height:884px;overflow:hidden;background:var(--page)}
  .stage{position:relative;width:1200px;height:884px}

  .hanger{position:absolute;top:150px;width:250px;height:580px;overflow:hidden;background:var(--white)}
  .hanger--front{left:290px}
  .hanger--back{left:660px}
  .handle-hole{position:absolute;left:90px;top:22px;width:70px;height:70px;border-radius:50%;background:var(--page);z-index:5}

  /* ---------- front ---------- */
  .hero-photo{position:absolute;left:0;top:0;width:250px;height:240px;
    background:linear-gradient(160deg,#e9e9e9 0%,#9a9a9a 45%,#5e5e5e 100%)}
  .chevron{position:absolute;left:0;top:0;width:250px;height:580px}
  .logo-plate{position:absolute;left:60px;top:116px;width:130px;height:76px;background:var(--white);
    display:flex;flex-direction:column;align-items:center;justify-content:center;gap:6px;text-align:center;z-index:2;padding:0 6px}
  .logo-mark{width:14px;height:14px;background:var(--teal)}
  .logo-name{font-family:var(--slab);font-weight:700;color:var(--teal);font-size:13px;line-height:1.1}

  .headline{position:absolute;left:0;top:276px;width:250px;text-align:center;font-family:var(--slab);font-weight:800;color:var(--white);line-height:1.02}
  .headline span{display:block}
  .hl-small{font-size:18px}
  .hl-teal{color:var(--teal)}
  .hl-big{font-size:31px}
  .hl-mid{font-size:17px}
  .hl-huge{font-size:35px}
  .address-box{position:absolute;left:75px;top:452px;width:100px;height:50px;border:1px solid var(--line)}
  .contact{position:absolute;left:0;top:508px;width:250px;text-align:center;font-family:var(--sans);color:var(--white);font-size:10px;line-height:1.35}
  .contact-row{display:flex;align-items:center;justify-content:center;gap:4px}
  .credentials{position:absolute;left:0;bottom:0;width:250px;height:38px;background:var(--white);
    display:flex;align-items:center;justify-content:space-around;padding:0 10px}
  .cred-badge{width:28px;height:18px;background:var(--ink)}
  .cred-seal{width:22px;height:22px;border-radius:50%;background:#c9c9c9}
  .cred-plate{width:56px;height:18px;background:#c8342b}
  .cred-name{font-family:var(--sans);font-weight:700;font-size:12px;color:var(--ink)}

  /* ---------- back ---------- */
  .services-title{position:absolute;left:0;top:104px;width:250px;text-align:center;font-family:var(--slab);font-weight:700;font-size:16px;color:var(--ink)}
  .service{position:absolute;width:100px;text-align:center;font-family:var(--slab);font-weight:600;font-size:11px;color:var(--ink);line-height:1}
  .service-photo{width:100px;height:82px}
  .service--roof{left:20px;top:128px}
  .service--gutter{left:130px;top:128px}
  .service--paint{left:20px;top:238px}
  .service--wash{left:130px;top:238px}
  .service-label{display:block;margin-bottom:4px}
  .service-label--below{margin:4px 0 0}
  .ph-roof{background:linear-gradient(170deg,#d9dde2,#6e6f70 55%,#8b7f70)}
  .ph-gutter{background:linear-gradient(180deg,#c8d4da,#7f858a 55%,#3d4144)}
  .ph-paint{background:linear-gradient(180deg,#b9bcbe,#8d8f90 50%,#2f3236)}
  .ph-wash{background:linear-gradient(180deg,#b09687,#9b9992 50%,#80796e)}

  .roof-panel{position:absolute;left:0;top:0;width:250px;height:580px}
  .award{position:absolute;left:104px;top:352px;width:42px;height:48px}
  .experience{position:absolute;left:0;top:406px;width:250px;text-align:center;font-family:var(--slab);font-weight:600;font-size:10.5px;color:var(--white);line-height:1.3}
  .logo-plate--small{left:75px;top:452px;width:100px;height:58px;gap:4px;padding:0 5px}
  .logo-plate--small .logo-mark{width:10px;height:10px}
  .logo-plate--small .logo-name{font-size:9.5px}
  .location{position:absolute;left:0;top:516px;width:250px;display:flex;align-items:center;justify-content:center;gap:4px;font-family:var(--slab);font-weight:600;font-size:10px;color:var(--white)}
  .payments{position:absolute;left:0;bottom:0;width:250px;height:40px;background:var(--white);text-align:center}
  .payments-title{font-family:var(--slab);font-weight:700;font-size:7px;color:var(--ink);padding-top:4px}
  .cards{display:flex;justify-content:center;gap:4px;margin-top:3px}
  .card{width:42px;height:18px;border:1px solid #cfcfcf;font-family:var(--sans);font-weight:700;font-size:7px;line-height:16px;color:var(--ink)}
</style>
</head>
<body>
<main class="stage">

  <section class="hanger hanger--front">
    <div class="hero-photo" role="img" aria-label="Black and white photo of a roofer installing shingles on a roof"></div>
    <svg class="chevron" viewBox="0 0 250 580" aria-hidden="true">
      <polygon points="0,168 125,250 250,168 250,580 0,580" fill="#ffffff"/>
      <polygon points="0,182 125,264 250,182 250,580 0,580" fill="#5c5c5c"/>
    </svg>
    <div class="handle-hole"></div>
    <div class="logo-plate">
      <span class="logo-mark"></span>
      <span class="logo-name">Quillby Housecrafters</span>
    </div>
    <h1 class="headline">
      <span class="hl-small">WE ARE</span>
      <span class="hl-big hl-teal">WORKING</span>
      <span class="hl-small">IN YOUR</span>
      <span class="hl-mid hl-teal">NEIGHBORHOOD,</span>
      <span class="hl-small">YOU CAN</span>
      <span class="hl-big">FIND US</span>
      <span class="hl-huge">US HERE</span>
    </h1>
    <div class="address-box"></div>
    <div class="contact">
      <div class="contact-row">
        <svg width="9" height="9" viewBox="0 0 10 10" aria-hidden="true"><circle cx="5" cy="5" r="5" fill="#33b8a4"/><path d="M3 2.5l1.2 0 .5 1.4-.7.6a4 4 0 0 0 1.5 1.5l.6-.7 1.4.5v1.2c-2.5.2-4.7-2-4.5-4.5z" fill="#fff"/></svg>
        (503) 555-0148
      </div>
      <div class="contact-row">
        <svg width="9" height="9" viewBox="0 0 10 10" aria-hidden="true"><circle cx="5" cy="5" r="5" fill="#33b8a4"/><rect x="2.5" y="3.3" width="5" height="3.4" fill="#fff"/></svg>
        hello@quillbyhousecrafters.com
      </div>
    </div>
    <div class="credentials">
      <span class="cred-badge"></span>
      <span class="cred-name">Ratewell</span>
      <span class="cred-seal"></span>
      <span class="cred-plate"></span>
    </div>
  </section>

  <section class="hanger hanger--back">
    <div class="handle-hole"></div>
    <h2 class="services-title">OUR SERVICES</h2>
    <figure class="service service--roof">
      <span class="service-label">ROOFING</span>
      <div class="service-photo ph-roof" role="img" aria-label="Photo of a finished shingle roof on a stone house"></div>
    </figure>
    <figure class="service service--gutter">
      <span class="service-label">GUTTERS</span>
      <div class="service-photo ph-gutter" role="img" aria-label="Photo of a crew member installing gutters"></div>
    </figure>
    <figure class="service service--paint">
      <div class="service-photo ph-paint" role="img" aria-label="Photo of a crew member painting house siding"></div>
      <span class="service-label service-label--below">PAINTING</span>
    </figure>
    <figure class="service service--wash">
      <div class="service-photo ph-wash" role="img" aria-label="Photo of a driveway being pressure washed"></div>
      <span class="service-label service-label--below">PRESSURE WASH</span>
    </figure>

    <svg class="roof-panel" viewBox="0 0 250 580" aria-hidden="true">
      <polygon points="0,398 125,340 250,398 250,580 0,580" fill="#5c5c5c"/>
    </svg>
    <svg class="award" viewBox="0 0 42 48" aria-hidden="true">
      <path d="M21 1 L40 7 V24 C40 36 31 43 21 47 C11 43 2 36 2 24 V7 Z" fill="#33a86a" stroke="#ffffff" stroke-width="2"/>
    </svg>
    <p class="experience">We have over 20years of experince<br>in the roofing industry we use<br>top quality materials</p>
    <div class="logo-plate logo-plate--small">
      <span class="logo-mark"></span>
      <span class="logo-name">Quillby Housecrafters</span>
    </div>
    <div class="location">
      <svg width="8" height="10" viewBox="0 0 8 10" aria-hidden="true"><path d="M4 0a4 4 0 0 1 4 4c0 3-4 6-4 6S0 7 0 4a4 4 0 0 1 4-4z" fill="#33b8a4"/><circle cx="4" cy="4" r="1.4" fill="#5c5c5c"/></svg>
      Portland, OR 97299, United States
    </div>
    <div class="payments">
      <p class="payments-title">FINANCING AVAILABLE</p>
      <div class="cards">
        <span class="card">Paylo</span>
        <span class="card">Cardex</span>
        <span class="card">Amberpay</span>
        <span class="card">Finvo</span>
      </div>
    </div>
  </section>

</main>
</body>
</html>
```